Book Cover Design Project for Thriller

I need a book cover for my thriller, 'Mara's Lantern.'

I will use this image primarily for e-publishing on e-readers, and hopefully someday on the front of a hardcover. It is very important that the image can be easily recognizable when it is in thumbnail view, just as one would see it while shopping online.

I would like my name, Paul T. Brand to be on the top of the image, and the title, Mara's Lantern, to be on the bottom. The title needs to be larger than my name so that it stands out more.

Requirements (taken from Quillo):
- Image dimensions of at least 500 by 800 pixels.
- A maximum of 2000 pixels on the longest side is preferred
- Ideal height/width ratio of 1.6

Images/items from the book that could be incorporated into the cover design are listed below in no particular order(please note: not all of these need to be included):
- Mountains & Forest (Story takes place in eastern Montana)
- Marine Corps emblem (Main character is a Marine)
- Red float plane flying over Montana, w/ engine on fire, going down.
- Silver Star military award
- Young man and young woman (both early 20s) holding hands while running through the woods and or mountains.
- A rifle (simple hunting type, no scope)
- A mountain stream

Here is a 'flap cover' summary of the book:
"Cole Durand returns home to Montana from a tour as a Marine in Afghanistan wanting to escape into the wilderness. Nina Harcourt is up and coming pop singer from Baltimore whose concert tour has sent her life into a downward spiral. When Cole disrupts the attempted kidnapping of Nina, he’s forced back into his familiar role as a Marine. Cole and Nina must evade her determined kidnappers through miles of uninhabited forests and mountains of western Montana. Despite their completely different lives, the two must learn to trust each other as they confront more than just the men who threaten to destroy them."

Thank you for considering this project!- Paul

```html
<!DOCTYPE html>
<html lang="en">
<head>
<meta charset="utf-8">
<title>Mara's Lantern — Book Cover</title>
<link rel="stylesheet" href="https://fonts.googleapis.com/css2?family=Bebas+Neue&family=Oswald:wght@500;700&display=swap">
<style>
  :root {
    --stage: #bdbdbd;
    --stage-light: #d6d6d6;
    --cover-black: #060606;
    --spine-black: #0b0b0b;
    --stripe: #e9e9e9;
    --blurb-top: #8a8a8a;
    --blurb-mid: #f2f2f2;
    --author-dark: #3a3a3a;
    --title-light: #e6e6e6;
    --author-light: #d9d9d9;
    --mist-light: #e4e4e4;
    --mist-mid: #a9a9a9;
    --forest-dark: #4a4a4a;
  }
  html, body {
    margin: 0;
    padding: 0;
    width: 1200px;
    height: 1200px;
    overflow: hidden;
  }
  body {
    background: radial-gradient(ellipse at 60% 40%, var(--stage-light), var(--stage) 75%);
    position: relative;
  }
  .book-wrap {
    position: absolute;
    left: 125px;
    top: 248px;
    width: 950px;
    height: 704px;
    display: flex;
    box-shadow: 0 18px 40px rgba(0,0,0,0.35);
  }
  .back-cover {
    position: relative;
    width: 440px;
    height: 100%;
    background: var(--cover-black);
  }
  .edge-stripe {
    position: absolute;
    right: 0;
    top: 0;
    width: 10px;
    height: 100%;
    background: var(--stripe);
  }
  .blurb {
    position: absolute;
    left: 36px;
    right: 40px;
    top: 190px;
    margin: 0;
    font-family: "Bebas Neue", "Oswald", sans-serif;
    font-size: 21px;
    line-height: 1.38;
    letter-spacing: 0.3px;
    text-align: center;
    text-transform: uppercase;
    background: linear-gradient(180deg, var(--blurb-top) 0%, var(--blurb-mid) 45%, var(--blurb-top) 100%);
    -webkit-background-clip: text;
    background-clip: text;
    color: transparent;
  }
  .spine {
    position: relative;
    width: 70px;
    height: 100%;
    background: var(--spine-black);
  }
  .spine-title {
    position: absolute;
    left: 30px;
    top: 28px;
    transform-origin: 0 0;
    transform: rotate(90deg) translateY(-50%);
    white-space: nowrap;
    font-family: "Oswald", sans-serif;
    font-weight: 700;
    font-size: 40px;
    letter-spacing: 1px;
    text-transform: uppercase;
    color: #ffffff;
    text-shadow: 2px 2px 0 #6a6a6a;
  }
  .spine-author {
    position: absolute;
    left: 30px;
    bottom: 110px;
    transform-origin: 0 0;
    transform: rotate(90deg) translateY(-50%);
    white-space: nowrap;
    font-family: "Bebas Neue", sans-serif;
    font-size: 15px;
    letter-spacing: 0.5px;
    color: var(--author-light);
  }
  .front-cover {
    position: relative;
    width: 440px;
    height: 100%;
    background: var(--cover-black);
  }
  .cover-art {
    position: absolute;
    inset: 0;
    clip-path: polygon(8% 3%, 95% 3%, 95% 84%, 34% 84%);
    background:
      linear-gradient(180deg, rgba(255,255,255,0.35) 0%, rgba(255,255,255,0) 40%),
      linear-gradient(90deg, var(--forest-dark) 0%, var(--mist-mid) 35%, var(--mist-light) 60%, var(--mist-mid) 85%, var(--forest-dark) 100%);
  }
  .cover-art::after {
    content: "";
    position: absolute;
    left: 0;
    right: 0;
    bottom: 16%;
    height: 24%;
    background: linear-gradient(180deg, rgba(60,60,60,0) 0%, rgba(60,60,60,0.75) 100%);
  }
  .front-author {
    position: absolute;
    left: 44px;
    right: 28px;
    top: 44px;
    margin: 0;
    font-family: "Bebas Neue", sans-serif;
    font-size: 26px;
    letter-spacing: 1px;
    text-align: center;
    color: var(--author-dark);
  }
  .front-title {
    position: absolute;
    left: 20px;
    right: 20px;
    top: 614px;
    margin: 0;
    font-family: "Oswald", sans-serif;
    font-weight: 700;
    font-size: 50px;
    line-height: 1;
    text-align: center;
    text-transform: uppercase;
    color: var(--title-light);
  }
</style>
</head>
<body>
  <main class="book-wrap">
    <section class="back-cover">
      <p class="blurb">Cole Durand returns home to Montana from a tour as a Marine in Afghanistan wanting to escape into the wilderness. Nina Harcourt is up and coming pop singer from Baltimore whose concert tour has sent her life into a downward spiral. When Cole disrupts the attempted kidnapping of Nina, he's forced back into his familiar role as a Marine. Cole and Nina must evade her determined kidnappers through miles of uninhabited forests and mountains of western Montana. Despite their completely different lives, the two must learn to trust each other as they confront more than just the men who threaten to destroy them.</p>
      <div class="edge-stripe"></div>
    </section>
    <section class="spine">
      <span class="spine-title">Mara's Lantern</span>
      <span class="spine-author">Paul T. Brand</span>
      <div class="edge-stripe"></div>
    </section>
    <section class="front-cover">
      <div class="cover-art" role="img" aria-label="Misty black and white pine forest with a faint figure among the trees"></div>
      <p class="front-author">Paul T. Brand</p>
      <h1 class="front-title">Mara's Lantern</h1>
    </section>
  </main>
</body>
</html>
```